Law Firm Stationery Design Project

This is the final part of a law firm rebrand project. The logo design is near completion, and I am also asking for business card designs in a separate contest. I will post the winning logo design to this project sometime tomorrow.

The job here is to design letterhead, business envelopes, shipping labels, memorandum, report, and the like, based on the following criteria (mainly quoted from the business card project):

My firm specializes in representing startup companies. This means I routinely interact with young entrepreneurs and the (typically) older, more experienced investors who fund them. I need to appeal to the former without offending the latter. I'm interesting in conveying the idea that my firm is a credible alternative to larger, brand-name firms. I use these words in positioning my firm in this market: creative; flexible; fair; practical; experienced. The winning design needs to convey this idea.

I'm will also be re-working my website soon and will likely use noto sans and noto serif as my primary website fonts. I'd like the stationary (just as I have asked the same of the business card) to use a font that is similar, but also compatible with the font used in the firm's logo.

Target Market(s)

Young entrepreneurs and older investors who collaborate in the formation and funding of high-tech startup companies located in the Pacific Northwest.

Industry/Entity Type

Law Firm

Font styles to use
Serif
Sans Serif

Requirements
Must have
• - Firm logo, firm tag line, return mailing address, firm website url, firm phone number, attorney name, attorney title, attorney email address, and attorney twitter account. I will provide the specific contact information to the winning designer; you may use fictional data in preparing your design.

The attached pdf for a proposed business card indicates the kind of tone that I have in mind, recognizing that it is my amateur attempt at doing what I'm hoping the winning designer is able to do so much better.

```html
<!DOCTYPE html>
<html lang="en">
<head>
<meta charset="utf-8">
<title>Harlow Law PLLC — Stationery</title>
<link rel="stylesheet" href="https://fonts.googleapis.com/css2?family=Montserrat:wght@400;500&family=Noto+Sans:wght@400;700&display=swap">
<style>
  :root{
    --navy-dark:#1d3a5c;
    --navy:#1b4a7c;
    --navy-light:#1f5a94;
    --paper:#ffffff;
    --backdrop:#e8e9eb;
    --ink:#2c4e78;
    --ink-soft:#6e7f93;
    --rule:#b9c0c9;
    --on-navy:#dfe7f1;
  }
  *{box-sizing:border-box;margin:0;padding:0}
  html,body{width:1200px;height:869px;overflow:hidden}
  body{background:var(--backdrop);position:relative;font-family:"Noto Sans",sans-serif;color:var(--ink)}
  .sheet{position:absolute;background:var(--paper);box-shadow:0 2px 6px rgba(0,0,0,.12)}
  .sheet--navy{background:linear-gradient(160deg,var(--navy-dark),var(--navy-light));color:var(--on-navy)}

  .wordmark{font-family:"Montserrat",sans-serif;font-weight:500;letter-spacing:.08em;text-transform:uppercase;white-space:nowrap;line-height:1}
  .tagline{font-family:"Montserrat",sans-serif;font-weight:400;letter-spacing:.12em;text-transform:uppercase;white-space:nowrap}

  /* Letterhead */
  .letterhead{left:60px;top:60px;width:340px;height:480px}
  .letterhead .brand{position:absolute;top:40px;left:0;right:0;text-align:center}
  .letterhead .wordmark{font-size:13px;color:var(--ink)}
  .letterhead .tagline{font-size:5px;color:var(--ink-soft);margin-top:5px}
  .letterhead .footer{position:absolute;left:26px;right:26px;bottom:32px;border-top:1px solid var(--rule);padding-top:8px;text-align:center}
  .footer .attorney{font-size:6.5px;font-weight:700;color:var(--ink);letter-spacing:.04em}
  .footer .attorney span{font-weight:400;color:var(--ink-soft)}
  .footer p{font-size:5.5px;color:var(--ink-soft);margin-top:4px}
  .footer b{color:var(--ink)}

  /* Presentation folder */
  .folder{left:430px;top:60px;width:340px;height:480px}
  .folder .brand{position:absolute;top:110px;left:0;right:0;text-align:center}
  .folder .wordmark{font-size:18px;color:var(--on-navy)}
  .folder .tagline{font-size:6px;margin-top:7px;color:var(--on-navy)}
  .folder .url{position:absolute;bottom:28px;left:0;right:0;text-align:center;font-size:7px;letter-spacing:.06em}

  /* Business cards */
  .card{width:330px;height:188px;left:810px}
  .card--front{top:60px}
  .card--back{top:300px}
  .card--front .brand{position:absolute;left:26px;top:70px}
  .card--front .wordmark{font-size:12px;color:var(--ink)}
  .card--front .tagline{font-size:4.5px;color:var(--ink-soft);margin-top:5px}
  .card--front .details{position:absolute;left:190px;top:58px;font-size:6px;color:var(--ink-soft);line-height:1.6}
  .card--front .details .name{font-size:7.5px;font-weight:700;color:var(--ink);letter-spacing:.04em}
  .card--front .details .title{margin-bottom:6px}
  .card--back .brand{position:absolute;left:0;right:0;top:64px;text-align:center}
  .card--back .wordmark{font-size:14px}
  .card--back .tagline{font-size:5px;margin-top:6px}
  .card--back .values{position:absolute;left:0;right:0;bottom:28px;text-align:center;font-size:6px;letter-spacing:.08em;line-height:1.6}

  /* Envelopes */
  .envelope{width:520px;height:240px;top:590px}
  .envelope--plain{left:60px}
  .envelope--plain .brand{position:absolute;left:30px;top:28px}
  .envelope--plain .wordmark{font-size:13px;color:var(--ink)}
  .envelope--plain .tagline{font-size:5px;color:var(--ink-soft);margin-top:5px}
  .envelope--plain .return{position:absolute;left:30px;top:78px;border-top:1px solid var(--rule);padding-top:6px;width:90px;font-size:5.5px;color:var(--ink-soft);line-height:1.6}
  .envelope--flap{left:620px;overflow:hidden}
  .envelope--flap .flap{position:absolute;left:0;top:0;width:100%;height:92px;background:linear-gradient(160deg,var(--navy-dark),var(--navy-light));display:flex;align-items:center;justify-content:center}
  .envelope--flap .wordmark{font-size:11px;color:var(--on-navy)}
</style>
</head>
<body>

<section class="sheet letterhead" aria-label="Letterhead">
  <div class="brand">
    <div class="wordmark">Harlow Law PLLC</div>
    <div class="tagline">Counsel for the Startup Company</div>
  </div>
  <div class="footer">
    <div class="attorney">REID A. HARLOW · <span>Startup Attorney</span></div>
    <p>1120 Cedar Avenue, Kirkland, WA 98033 &nbsp; <b>Tel</b> 425.555.0142</p>
    <p><b>Twitter</b> @reidharlow &nbsp; <b>Email</b> reid@harlowlawpllc.com &nbsp; <b>Web</b> harlowlawpllc.com</p>
  </div>
</section>

<section class="sheet sheet--navy folder" aria-label="Presentation folder">
  <div class="brand">
    <div class="wordmark">Harlow Law PLLC</div>
    <div class="tagline">Counsel for the Startup Company</div>
  </div>
  <div class="url">www.harlowlawpllc.com</div>
</section>

<section class="sheet card card--front" aria-label="Business card front">
  <div class="brand">
    <div class="wordmark">Harlow Law PLLC</div>
    <div class="tagline">Counsel for the Startup Company</div>
  </div>
  <div class="details">
    <div class="name">REID A. HARLOW</div>
    <div class="title">Startup Attorney</div>
    <div>1120 Cedar Avenue</div>
    <div>Kirkland, WA 98033</div>
    <div>425.555.0142</div>
    <div>reid@harlowlawpllc.com</div>
    <div>@reidharlow</div>
  </div>
</section>

<section class="sheet sheet--navy card card--back" aria-label="Business card back">
  <div class="brand">
    <div class="wordmark">Harlow Law PLLC</div>
    <div class="tagline">Counsel for the Startup Company</div>
  </div>
  <div class="values">Creative · Flexible · Fair<br>Practical · Experienced</div>
</section>

<section class="sheet envelope envelope--plain" aria-label="Business envelope">
  <div class="brand">
    <div class="wordmark">Harlow Law PLLC</div>
    <div class="tagline">Counsel for the Startup Company</div>
  </div>
  <div class="return">1120 Cedar Avenue<br>Kirkland, WA 98033</div>
</section>

<section class="sheet envelope envelope--flap" aria-label="Envelope back with flap">
  <div class="flap"><div class="wordmark">Harlow Law PLLC</div></div>
</section>

</body>
</html>
```